Quiver Upcoming Gigs

One page graphic with my upcoming dates. Logo and photo attached, and sample from last flyer. Text:

QUIVER

UPCOMING DATES

3/26/18 Velvet Grotto (Las Vegas, NV)

4/1/18 Lantern Hall 2847 M St (Sac, CA)

4/8/18 Blue Heron (Sac, CA)

5/5/18 Open Lanes @ Silver Otter (Sac, CA)

5/10/18 Dunmore Fine Gallery (Sac, CA)

5/11/18 Bas Rive @ Cafe du Pont (Sac, CA)

5/27/18 Sunloft LBW @ Vox (Sac, CA)

Save The Date: 9/21/18 Moonweaver Festival (Puerto Nuevo, MX)

fanwall.net/quiver530

Target Market(s)

House/Electronic Music

Industry/Entity Type

Night Club

Font styles to use
Sans Serif

Colors

Designer to choose colors to be used in the design.

Requirements
Must have
• Quiver logo or something that looks good instead. Prefer photo to be in but not necessary.
Nice to have

```html
<!DOCTYPE html>
<html lang="en">
<head>
<meta charset="utf-8">
<title>Quiver – Upcoming Dates</title>
<link href="https://fonts.googleapis.com/css2?family=Montserrat:wght@200;400;700;900&display=swap" rel="stylesheet">
<style>
  :root {
    --ink: #000000;
    --paper: #ffffff;
    --glow-violet: #4a2fb0;
    --glow-magenta: #b0306e;
    --glow-warm: #d9826e;
    --shade: #12081c;
  }
  html, body {
    margin: 0;
    padding: 0;
    overflow: hidden;
    background: var(--ink);
  }
  .flyer {
    position: relative;
    width: 1200px;
    height: 627px;
    overflow: hidden;
    background: var(--ink);
    color: var(--paper);
    font-family: "Montserrat", sans-serif;
  }
  .dj-photo {
    position: absolute;
    left: 560px;
    top: 0;
    width: 640px;
    height: 627px;
    background:
      linear-gradient(to right, var(--ink) 0%, rgba(0,0,0,0) 22%),
      radial-gradient(ellipse 180px 220px at 290px 320px, var(--glow-warm) 0%, rgba(176,48,110,0.7) 45%, rgba(0,0,0,0) 100%),
      radial-gradient(ellipse 320px 260px at 230px 110px, var(--glow-violet) 0%, rgba(74,47,176,0.35) 55%, rgba(0,0,0,0) 100%),
      radial-gradient(ellipse 360px 200px at 420px 430px, var(--glow-magenta) 0%, rgba(0,0,0,0) 100%),
      linear-gradient(180deg, var(--shade) 0%, #1a0a22 60%, #050207 100%);
  }
  .brand-mark {
    position: absolute;
    left: 55px;
    top: 68px;
    width: 92px;
    height: 470px;
  }
  .brand-name {
    position: absolute;
    left: 50%;
    top: 50%;
    transform: translate(-50%, -50%) rotate(-90deg);
    font-weight: 900;
    font-size: 106px;
    line-height: 1;
    letter-spacing: 6px;
    white-space: nowrap;
    color: var(--paper);
  }
  .headline {
    position: absolute;
    left: 156px;
    top: 58px;
    margin: 0;
    line-height: 1;
    text-transform: uppercase;
  }
  .headline-light {
    display: block;
    font-weight: 200;
    font-size: 62px;
    letter-spacing: -0.5px;
  }
  .headline-bold {
    display: block;
    font-weight: 700;
    font-size: 56px;
    letter-spacing: -1px;
    margin-top: -3px;
  }
  .gig-list {
    position: absolute;
    left: 158px;
    top: 200px;
    margin: 0;
    padding: 0;
    list-style: none;
  }
  .gig {
    height: 37px;
    font-size: 18px;
    white-space: nowrap;
  }
  .gig-date { font-weight: 400; }
  .gig-venue { font-weight: 700; }
  .gig-place { font-weight: 400; font-size: 14.5px; }
  .save-label {
    position: absolute;
    left: 158px;
    top: 479px;
    font-weight: 700;
    font-size: 17px;
  }
  .save-gig {
    position: absolute;
    left: 158px;
    top: 514px;
  }
  .social {
    position: absolute;
    left: 806px;
    top: 534px;
    display: flex;
    align-items: center;
    gap: 14px;
  }
  .social-dot {
    width: 48px;
    height: 48px;
    border-radius: 50%;
    background: var(--paper);
  }
  .social-handle {
    font-size: 22px;
    font-weight: 400;
  }
</style>
</head>
<body>
<main class="flyer">
  <div class="dj-photo" role="img" aria-label="DJ in a white t-shirt and cap mixing on turntables under purple and pink club lights against a brick wall"></div>

  <div class="brand-mark"><span class="brand-name">QUIVER</span></div>

  <h1 class="headline">
    <span class="headline-light">Upcoming</span>
    <span class="headline-bold">Dates</span>
  </h1>

  <ul class="gig-list">
    <li class="gig"><span class="gig-date">3/26/18</span> <span class="gig-venue">Velvet Grotto</span> <span class="gig-place">(Las Vegas, NV)</span></li>
    <li class="gig"><span class="gig-date">4/1/18</span> <span class="gig-venue">Lantern Hall 2847 M St</span> <span class="gig-place">(Sac, CA)</span></li>
    <li class="gig"><span class="gig-date">4/8/18</span> <span class="gig-venue">Blue Heron</span> <span class="gig-place">(Sac, CA)</span></li>
    <li class="gig"><span class="gig-date">5/5/18</span> <span class="gig-venue">Open Lanes @ Silver Otter</span> <span class="gig-place">(Sac, CA)</span></li>
    <li class="gig"><span class="gig-date">5/10/18</span> <span class="gig-venue">Dunmore Fine Gallery</span> <span class="gig-place">(Sac, CA)</span></li>
    <li class="gig"><span class="gig-date">5/11/18</span> <span class="gig-venue">Bas Rive @ Cafe du Pont</span> <span class="gig-place">(Sac, CA)</span></li>
    <li class="gig"><span class="gig-date">5/27/18</span> <span class="gig-venue">Sunloft LBW @ Vox</span> <span class="gig-place">(Sac, CA)</span></li>
  </ul>

  <div class="save-label">Save The Date:</div>
  <div class="gig save-gig"><span class="gig-date">9/21/18</span> <span class="gig-venue">Moonweaver Festival</span> <span class="gig-place">(Puerto Nuevo, MX)</span></div>

  <div class="social">
    <span class="social-dot"></span>
    <span class="social-handle">fanwall.net/quiver530</span>
  </div>
</main>
</body>
</html>
```